Business card design for counselling and psychotherapy practice

I am seeking a business card for a new venture into private practice. I am based in Brisbane Qld Australia. I provide holistic counselling and psychotherapy to individuals and groups.
Some words that describe the underpinnings of this practice would include: being, becoming, awareness, wholeness, contact, safety, acceptance, relationship, gestalt, paradox, interconnected, nature, process.
I would like to see designs that include earth colours.
The overall design should communicate safety and a curiosity of being and becoming.
Target Market(s)
this design is marketed toward women, professionals, lesbian, transgender, mothers
Industry/Entity Type
Safety
Contact Information for Business Card
Still Harbour
Counselling and Psychotherapy
Wren Callow
ph: 0412739506
email: wren.stillharbour@examplemail.test
www.stillharbourcounselling&psychotherapy.test
Logo styles of interest
Abstract Logo
Look and feel

```html
<!DOCTYPE html>
<html lang="en">
<head>
<meta charset="utf-8">
<title>Still Harbour — Business Card</title>
<link href="https://fonts.googleapis.com/css2?family=Arimo:wght@400;700&family=Tinos&display=swap" rel="stylesheet">
<style>
  :root {
    --canvas: #e9e6e2;
    --card-front: #b79b88;
    --card-front-light: #c4aa98;
    --card-back: #fbfaf8;
    --ink-dark: #3b2417;
    --ink-mid: #4a3022;
    --accent: #c9852e;
    --band: #7a5430;
  }
  * { margin: 0; padding: 0; box-sizing: border-box; }
  html, body { width: 1200px; height: 900px; overflow: hidden; }
  body {
    background: var(--canvas);
    font-family: "Arimo", Arial, sans-serif;
    position: relative;
  }
  .card {
    position: absolute;
    left: 320px;
    width: 560px;
    height: 320px;
    overflow: hidden;
    box-shadow: 0 10px 26px rgba(0,0,0,0.22);
  }
  .card--front { top: 60px; background: var(--card-front); }
  .card--back { top: 470px; background: var(--card-back); }

  .front-curves { position: absolute; inset: 0; }

  .brand {
    position: absolute;
    display: flex;
    align-items: center;
    gap: 14px;
  }
  .brand-mark { background: var(--accent); flex: none; }
  .brand-name {
    font-family: "Tinos", "Times New Roman", serif;
    color: var(--ink-dark);
    line-height: 1;
    white-space: nowrap;
  }
  .brand-tagline {
    position: absolute;
    color: var(--ink-mid);
    letter-spacing: 0.08em;
    white-space: nowrap;
  }

  .card--front .brand { left: 88px; top: 104px; }
  .card--front .brand-mark { width: 58px; height: 58px; }
  .card--front .brand-name { font-size: 54px; }
  .card--front .brand-tagline { left: 88px; top: 186px; font-size: 21px; }

  .card--back .brand { left: 36px; top: 30px; }
  .card--back .brand-mark { width: 36px; height: 36px; }
  .card--back .brand-name { font-size: 34px; }
  .card--back .brand-tagline { left: 36px; top: 82px; font-size: 13px; }

  .holder {
    position: absolute;
    top: 140px;
    left: 0; right: 0;
    text-align: center;
    font-weight: 700;
    font-size: 19px;
    color: var(--ink-dark);
  }
  .contact {
    position: absolute;
    top: 186px;
    left: 0; right: 0;
    text-align: center;
    font-size: 12.5px;
    line-height: 1.45;
    letter-spacing: 0.04em;
    color: var(--ink-dark);
    list-style: none;
  }
  .band {
    position: absolute;
    left: 0; right: 0; bottom: 0;
    height: 26px;
    background: var(--band);
  }
</style>
</head>
<body>
  <section class="card card--front" aria-label="Business card front">
    <svg class="front-curves" width="560" height="320" viewBox="0 0 560 320" aria-hidden="true">
      <circle cx="520" cy="-40" r="260" fill="var(--card-front-light)" opacity="0.55"/>
      <circle cx="60" cy="420" r="230" fill="var(--card-front-light)" opacity="0.35"/>
    </svg>
    <div class="brand">
      <span class="brand-mark"></span>
      <span class="brand-name">Still Harbour</span>
    </div>
    <p class="brand-tagline">Counselling and Psychotherapy</p>
  </section>

  <section class="card card--back" aria-label="Business card back">
    <div class="brand">
      <span class="brand-mark"></span>
      <span class="brand-name">Still Harbour</span>
    </div>
    <p class="brand-tagline">Counselling and Psychotherapy</p>
    <h1 class="holder">Wren Callow</h1>
    <ul class="contact">
      <li>04 1273 9506</li>
      <li>wren.stillharbour@examplemail.test</li>
      <li>www.stillharbourcounselling&amp;psychotherapy.test</li>
    </ul>
    <div class="band"></div>
  </section>
</body>
</html>
```